Tequila Bottle Labels

We are a construction company that bottled our own tequila and would like a unique label for it! We already have our own company logo (linked below) and we want that logo somewhere on the bottle as well- it can be big or small. It was brewed & bottled in Southern California. Ideally it would have the year "2020," "Single Estate," & "100% Agave Azul" somewhere on the label.

Tequila / RMT / 2020

```html
<!DOCTYPE html>
<html lang="en">
<head>
<meta charset="utf-8">
<title>RMT Single Estate Tequila – Label Set</title>
<link rel="stylesheet" href="https://fonts.googleapis.com/css2?family=Rye&family=Montserrat:wght@600;700&family=Libre+Baskerville:ital,wght@0,400;0,700;1,400&family=Fira+Sans+Condensed:wght@700&family=Fira+Sans:wght@600&display=swap">
<style>
  :root {
    --navy-deep: #0c2a55;
    --navy-mid: #1a5391;
    --navy-light: #2465a6;
    --gold: #e8c25a;
    --gold-pale: #f6e3a0;
    --gold-dark: #b88a2a;
    --cream: #f3f1ea;
    --ink: #222;
    --page: #ffffff;
  }
  * { margin: 0; padding: 0; box-sizing: border-box; }
  html, body { width: 1200px; height: 930px; overflow: hidden; background: var(--page); }
  .sheet { position: relative; width: 1200px; height: 930px; }

  /* dimension guides */
  .dim { position: absolute; }
  .dim--h { height: 16px; border-left: 1px solid var(--ink); border-right: 1px solid var(--ink); }
  .dim--h::after { content: ""; position: absolute; left: 0; right: 0; top: 50%; border-top: 1px solid var(--ink); }
  .dim--v { width: 16px; border-top: 1px solid var(--ink); border-bottom: 1px solid var(--ink); }
  .dim--v::after { content: ""; position: absolute; top: 0; bottom: 0; left: 50%; border-left: 1px solid var(--ink); }
  .dim__text { position: absolute; font: 700 14px "Fira Sans", sans-serif; color: var(--ink); white-space: nowrap; }
  .dim--h .dim__text { left: 50%; top: -18px; transform: translateX(-50%); }
  .dim--v .dim__text { top: 50%; left: -14px; transform: translate(-50%, -50%) rotate(-90deg); }

  /* label stock */
  .label {
    position: absolute;
    background:
      radial-gradient(ellipse at 50% 40%, var(--navy-light) 0%, var(--navy-mid) 45%, var(--navy-deep) 100%);
    color: var(--cream);
    text-align: center;
    overflow: hidden;
  }
  .brand { font: 700 30px "Libre Baskerville", serif; color: var(--cream); letter-spacing: -1px; }
  .ornament { position: absolute; height: 10px; border-radius: 5px;
    background: linear-gradient(90deg, rgba(232,194,90,0), var(--gold) 50%, rgba(232,194,90,0)); opacity: .8; }

  /* front label */
  .label--front { left: 110px; top: 170px; width: 490px; height: 630px; }
  .label--front .brand { position: absolute; top: 50px; left: 0; right: 0; }
  .front__estate { position: absolute; top: 110px; left: 0; right: 0; font: 700 16px "Montserrat", sans-serif; letter-spacing: 4px; }
  .front__title {
    position: absolute; top: 140px; left: 0; right: 0;
    font: 400 82px "Rye", serif; letter-spacing: 1px; line-height: 1;
    background: linear-gradient(180deg, var(--gold-pale) 0%, var(--gold) 55%, var(--gold-dark) 100%);
    -webkit-background-clip: text; background-clip: text; color: transparent;
  }
  .front__agave-text { position: absolute; top: 245px; left: 0; right: 0; font: 700 17px "Montserrat", sans-serif; letter-spacing: 5px; }
  .front__illustration {
    position: absolute; left: 165px; top: 296px; width: 165px; height: 120px;
    background: radial-gradient(ellipse at 50% 80%, rgba(232,194,90,.55), rgba(232,194,90,0) 70%);
  }
  .front__origin { position: absolute; top: 444px; left: 0; right: 0; display: flex; justify-content: center; align-items: center; gap: 14px; }
  .front__year { font: italic 400 30px "Libre Baskerville", serif; color: var(--gold); }
  .front__rule { width: 1px; height: 52px; background: var(--gold); }
  .front__place { text-align: left; font: 700 14px/1.45 "Libre Baskerville", serif; letter-spacing: 1.2px; text-transform: uppercase; }
  .front__spec { position: absolute; top: 562px; left: 0; right: 0; font: 700 13px "Montserrat", sans-serif; letter-spacing: 3px; }
  .front__spec span { margin: 0 12px; color: var(--gold); }
  .front__band { position: absolute; left: 0; right: 0; bottom: 0; height: 25px;
    background: linear-gradient(90deg, var(--gold-dark), var(--gold-pale) 25%, var(--gold) 50%, var(--gold-pale) 75%, var(--gold-dark)); }

  /* back label */
  .label--back { left: 680px; top: 330px; width: 420px; height: 280px; }
  .back__frame { position: absolute; inset: 12px; border: 2px solid var(--gold); }
  .label--back .brand { position: absolute; top: 28px; left: 0; right: 0; font-size: 24px; }
  .back__name { position: absolute; top: 63px; left: 0; right: 0; font: 700 17px "Fira Sans Condensed", sans-serif; letter-spacing: 1px; color: var(--gold); }
  .back__copy { position: absolute; top: 86px; left: 40px; right: 40px; font: 600 12.6px/17.6px "Fira Sans", sans-serif; }
  .back__copy p + p { margin-top: 10px; }
</style>
</head>
<body>
<main class="sheet">

  <div class="dim dim--h" style="left:110px; top:112px; width:490px;"><span class="dim__text">3.5 in.</span></div>
  <div class="dim dim--v" style="left:62px; top:170px; height:630px;"><span class="dim__text">4.5 in.</span></div>

  <section class="label label--front" aria-label="Front label">
    <div class="brand">RMT</div>
    <div class="ornament" role="img" aria-label="Gold scroll flourish" style="left:40px; top:116px; width:110px;"></div>
    <div class="ornament" role="img" aria-label="Gold scroll flourish" style="right:40px; top:116px; width:110px;"></div>
    <div class="front__estate">SINGLE ESTATE</div>
    <h1 class="front__title">TEQUILA</h1>
    <div class="front__agave-text">100% AGAVE AZUL</div>
    <div class="front__illustration" role="img" aria-label="Gold line illustration of an agave plant"></div>
    <div class="front__origin">
      <span class="front__year">2020</span>
      <span class="front__rule"></span>
      <span class="front__place">Bottled in<br>Southern California</span>
    </div>
    <div class="ornament" role="img" aria-label="Gold scroll flourish" style="left:182px; top:514px; width:125px;"></div>
    <div class="front__spec">40% ALC/ VOL (80 PROOF)<span>|</span>750 ML</div>
    <div class="front__band"></div>
  </section>

  <div class="dim dim--h" style="left:680px; top:272px; width:420px;"><span class="dim__text">3 in.</span></div>
  <div class="dim dim--v" style="left:640px; top:330px; height:280px;"><span class="dim__text">2 in.</span></div>

  <section class="label label--back" aria-label="Back label">
    <div class="back__frame"></div>
    <div class="ornament" role="img" aria-label="Gold scroll flourish" style="left:60px; top:48px; width:90px;"></div>
    <div class="ornament" role="img" aria-label="Gold scroll flourish" style="right:60px; top:48px; width:90px;"></div>
    <div class="brand">RMT</div>
    <div class="back__name">REPOSADO VALIENTE</div>
    <div class="back__copy">
      <p>Our reposado tequila has been cast and aged in premium oak bourbon barrels for 10 months to create the perfect golden amber color. The inviting aroma of sweet caramel is enticing and leaves your palette with smooth, elegant hints of oak and spice – making this tequila perfect for any occasion.</p>
      <p>Hecho en Jalisco, MX. Bourbon Barrel Aged in Huntington Beach, CA.</p>
    </div>
  </section>

</main>
</body>
</html>
```